MLD Illustration Web Design

Create illustration web design company for Mandirasa Luhur Digital (MLD). I more prefer design with illustration concept. Detail for requirement please see attach file. I'm also attach MLD logo. This logo had 2 type, 2D design and 3D design. You can chose one of them, or used both.
For the winner or had good design would be possible to private project to completeness this website
Attach file requirement is guidance for design, but any changes are welcome
Updates
Sorry, I forgot about contact. Please add menu contact. You can put this menu besides login menu or part of menu level #1, or put on some where to adjust your design. Menu contact will give pop up window to email MLD Company and Company Information (Address, Telephone, etc)
Target Market(s)
Company (Business To Business)
Industry/Entity Type
It Company
Look and feel
Each slider illustrates characteristics of the customer's brand and the style your logo design should communicate.

```html
<!DOCTYPE html>
<html lang="en">
<head>
<meta charset="utf-8">
<title>Mandirasa Luhur Digital — Software Development</title>
<link rel="stylesheet" href="https://fonts.googleapis.com/css2?family=Arimo:wght@400;700&display=swap">
<style>
  :root {
    --brand-blue: #0b6496;
    --brand-blue-dark: #075a88;
    --brand-green: #7aaa34;
    --brand-green-btn: #7fb23c;
    --sky-top: #9edcf0;
    --sky-bottom: #c4ecf6;
    --grass-light: #c4f07c;
    --grass-mid: #8cce3a;
    --footer-green: #5b9c14;
    --footer-green-deep: #4d8a0f;
    --footer-bar: #4a840d;
    --text-body: #555b60;
    --text-link: #0b6496;
    --white: #ffffff;
  }
  * { box-sizing: border-box; margin: 0; padding: 0; }
  html, body { width: 1200px; height: 1050px; overflow: hidden; }
  body {
    position: relative;
    font-family: "Arimo", Arial, sans-serif;
    background: linear-gradient(180deg, var(--sky-top) 0%, var(--sky-bottom) 62%, var(--sky-bottom) 66%);
  }
  .top-strip { position: absolute; left: 0; top: 0; width: 1200px; height: 7px; background: var(--brand-blue); }
  .account-tab {
    position: absolute; left: 757px; top: 0; width: 277px; height: 35px;
    background: var(--brand-blue);
    clip-path: polygon(0 0, 100% 0, 93% 100%, 7% 100%);
    display: flex; align-items: center; justify-content: center; gap: 18px;
    color: var(--white); font-weight: 700; font-size: 14.5px;
  }
  .account-tab .divider { width: 0; height: 24px; border-left: 1px dotted rgba(255,255,255,.5); }
  .logo {
    position: absolute; left: 162px; top: 30px;
    display: flex; align-items: center; gap: 12px;
  }
  .logo-mark { width: 60px; height: 60px; border-radius: 50%; background: var(--brand-blue); }
  .logo-name { font-size: 58px; font-weight: 700; color: var(--brand-green); letter-spacing: 2px; line-height: 1; }

  .landscape {
    position: absolute; left: 0; top: 630px; width: 1200px; height: 150px;
    background: linear-gradient(180deg, rgba(140,206,58,0) 0%, rgba(140,206,58,.6) 28%, var(--grass-light) 50%, var(--grass-mid) 78%, var(--footer-green) 100%);
  }
  .footer {
    position: absolute; left: 0; top: 776px; width: 1200px; height: 230px;
    background: linear-gradient(180deg, var(--footer-green) 0%, var(--footer-green-deep) 100%);
    color: var(--white);
  }
  .footer-col { position: absolute; top: 62px; }
  .footer-col h3 {
    font-size: 13px; font-weight: 700; letter-spacing: .3px;
    width: 140px; padding-bottom: 4px; border-bottom: 1px dotted rgba(255,255,255,.55);
  }
  .footer-col ul { list-style: none; margin-top: 16px; }
  .footer-col li { font-size: 11.5px; line-height: 16.6px; }
  .useful-links { left: 210px; }
  .categories { left: 522px; }
  .social { left: 828px; top: 59px; }
  .social ul { margin-top: 10px; }
  .social li {
    display: flex; align-items: center; gap: 12px;
    width: 152px; height: 29px; border-bottom: 1px solid rgba(255,255,255,.12);
  }
  .social li:last-child { border-bottom: none; }
  .social .badge { width: 17px; height: 17px; border-radius: 2px; background: #e4eef5; }
  .copyright {
    position: absolute; left: 0; top: 1006px; width: 1200px; height: 44px;
    background: var(--footer-bar); color: var(--white);
    font-size: 11.5px; text-align: center; line-height: 44px;
  }

  .feature-panel {
    position: absolute; left: 138px; top: 174px; width: 811px; height: 543px;
    background: var(--white); border-radius: 3px;
    box-shadow: 0 0 10px rgba(0,0,0,.12), inset 0 0 30px rgba(0,0,0,.05);
  }
  .feature-text { position: absolute; left: 34px; top: 42px; width: 325px; color: var(--text-body); }
  .feature-text h1 { font-size: 26px; font-weight: 700; color: var(--brand-green); margin-bottom: 17px; }
  .feature-text p { font-size: 12.4px; line-height: 16.6px; margin-bottom: 16.6px; }
  .feature-text a { color: var(--text-link); text-decoration: none; }
  .feature-list { list-style: none; margin-top: 20px; }
  .feature-list li { position: relative; padding-left: 14px; font-size: 12.4px; line-height: 22.2px; }
  .feature-list li::before {
    content: ""; position: absolute; left: 1px; top: 8px;
    border-left: 4px solid var(--brand-blue); border-top: 3px solid transparent; border-bottom: 3px solid transparent;
  }
  .feature-illustration {
    position: absolute; left: 388px; top: 57px; width: 397px; height: 424px;
    border-radius: 50% 50% 8px 8px / 40% 40% 8px 8px;
    background: radial-gradient(ellipse at 50% 45%, #f4f4f4 0%, #e2e6ea 55%, #d3d8de 100%);
  }
  .slider-dots { position: absolute; left: 374px; top: 506px; display: flex; gap: 5px; }
  .slider-dots span { width: 17px; height: 17px; border-radius: 50%; background: var(--brand-blue); }
  .slider-dots .active { background: var(--white); border: 4px solid var(--brand-green); }

  .main-nav { position: absolute; left: 958px; top: 179px; list-style: none; }
  .main-nav li {
    width: 103px; height: 30px; margin-bottom: 7.8px;
    background: var(--brand-blue); color: var(--white);
    border: 1px solid var(--brand-blue-dark);
    font-size: 15px; font-weight: 700; text-align: center; line-height: 28px;
  }
  .main-nav li.current { background: var(--brand-green-btn); border-color: #6e9e30; }
</style>
</head>
<body>
  <div class="top-strip"></div>
  <nav class="account-tab">
    <span>Sign In</span><span class="divider"></span><span>Register Now!</span>
  </nav>
  <div class="logo">
    <span class="logo-mark"></span>
    <span class="logo-name">MLD</span>
  </div>

  <div class="landscape"></div>

  <section class="feature-panel">
    <div class="feature-text">
      <h1>Software Development</h1>
      <p>Lorem ipsum dolor sit amet. Sed do eiusmod tempoLorem ipsum dolor sit amet, consectetur <a href="#">adipisicing elit, sed do eiusmod tempor incididunt</a> at labore et dolore magna aliqua.</p>
      <p>Ut enim ad minim veniam, quis nostrud exercitation ullamco laboris nisi ut aliquip ex ea commodo consequat.</p>
      <p>Duis aute irure dolor <a href="#">in reprehenderit in voluptate</a> velit esse cillum dolore eu fugiat nulla pariatur. Excepteur sint occaecat cupidatat non proident.</p>
      <ul class="feature-list">
        <li>Sed do eiusmod tempo</li>
        <li>Lorem ipsum dolor sit amet consectetur</li>
        <li>Adipisicing elit,</li>
        <li>Red do eiusmod tempor incididunt</li>
        <li>Ut labore et dolore magna</li>
      </ul>
    </div>
    <div class="feature-illustration" role="img" aria-label="Circular word cloud of software terms around the word SOFTWARE, with silhouettes of three business people in front"></div>
    <div class="slider-dots"><span class="active"></span><span></span><span></span><span></span></div>
  </section>

  <ul class="main-nav">
    <li>Home</li>
    <li class="current">SERVICES</li>
    <li>Product</li>
    <li>Clients</li>
    <li>Company</li>
    <li>Blog</li>
  </ul>

  <footer class="footer">
    <div class="footer-col useful-links">
      <h3>USEFUL LINKS</h3>
      <ul>
        <li>Home</li><li>Products</li><li>Accessories</li><li>Our Story</li><li>Questions</li><li>Blog</li><li>Where We Are</li>
      </ul>
    </div>
    <div class="footer-col categories">
      <h3>CATEGORIES</h3>
      <ul>
        <li>LInk-1</li><li>LInk-1</li><li>LInk-1</li><li>LInk-1</li><li>LInk-1</li><li>LInk-1</li><li>LInk-1</li>
      </ul>
    </div>
    <div class="footer-col social">
      <h3>SOCIAL NETWORK</h3>
      <ul>
        <li><span class="badge"></span>Bolg : @mld</li>
        <li><span class="badge"></span>Join us on Friendbook</li>
        <li><span class="badge"></span>Join us on WorkLinks</li>
        <li><span class="badge"></span>Chirper : @mld</li>
      </ul>
    </div>
  </footer>
  <div class="copyright">© 2007–2013, mandirasa-digital.net. All Rights Reserved</div>
</body>
</html>
```